Bref créative |
Jewelry and Home ware website | ||
Studio Kelvara | ||
Jewelry | ||
www.studiokelvara.example | ||
Studio Kelvara is a new company which is just about to launch to the public. Studio Kelvara is a line of handmade jewelry and home ware made with semi precious materials. All pieces are designed and made by me (kela) Rosalind Theda Quarrington. At the moment the brand is very small and the website will be primary used as an online catalogue, eventually hoping to start online buying. | ||
Clean and simple designs, nothing to distract from pieces. |
Clean/Simple Conservative Elegant Traditional Feminine |
Browns | ||
Beiges /Off Whites | ||
Natural tones | ||
left side | ||
View logo on company url. | ||

```html
<!DOCTYPE html>
<html lang="en">
<head>
<meta charset="utf-8">
<title>Studio Kelvara — Fine handcrafted Jewellery &amp; Homeware</title>
<link rel="stylesheet" href="https://fonts.googleapis.com/css2?family=Great+Vibes&family=Playfair+Display:ital,wght@0,400;1,400;1,700&family=Cinzel:wght@400&display=swap">
<style>
  :root {
    --wood-dark: #2a160d;
    --wood-mid: #4a2a19;
    --wood-light: #5c3520;
    --bar: #241109;
    --footer: #2e1a10;
    --gold: #e9a64a;
    --gold-soft: #c98a3d;
    --cream: #f4e6cc;
    --muted: #b89a78;
    --field: #1c0d06;
    --field-line: #6b4a30;
  }
  * { box-sizing: border-box; margin: 0; padding: 0; }
  html, body { width: 1200px; height: 830px; overflow: hidden; }
  body {
    position: relative;
    font-family: "Playfair Display", Georgia, serif;
    color: var(--cream);
    background: linear-gradient(100deg, var(--wood-dark) 0%, var(--wood-mid) 30%, var(--wood-light) 55%, var(--wood-mid) 80%, var(--wood-dark) 100%);
  }

  /* Top navigation */
  .site-nav {
    position: absolute; left: 0; top: 0; width: 1200px; height: 50px;
    background: linear-gradient(180deg, #3a1f12, var(--bar));
    box-shadow: 0 3px 8px rgba(0,0,0,.5);
  }
  .site-nav ul {
    position: absolute; left: 146px; top: 16px; width: 750px; list-style: none;
    display: flex; align-items: center; white-space: nowrap;
  }
  .site-nav li {
    font-style: italic; font-weight: 700; font-size: 14px; line-height: 18px; color: var(--gold);
    display: flex; align-items: center;
  }
  .site-nav li + li::before {
    content: ""; width: 4px; height: 4px; border-radius: 50%; background: var(--gold-soft);
    margin: 0 13px;
  }
  .site-nav li.is-current { color: var(--cream); text-decoration: underline; }
  .search { position: absolute; left: 912px; top: 15px; display: flex; gap: 6px; }
  .search .search-field { width: 118px; height: 20px; background: #f3ede4; border: 1px solid #8a6a4a; }
  .search .search-go {
    height: 20px; padding: 0 8px; font-size: 12px; line-height: 18px;
    background: linear-gradient(180deg, #7a5234, #4a2c19); color: var(--cream); border: 1px solid #8a6a4a;
  }

  /* Hero */
  .brand {
    position: absolute; left: 144px; top: 90px; width: 460px; text-align: center;
  }
  .brand-name {
    font-family: "Cinzel", Georgia, serif; font-size: 58px; line-height: 1.1; color: var(--cream);
    letter-spacing: 3px;
  }
  .brand-mark {
    display: inline-block; width: 14px; height: 14px; border-radius: 50%; background: var(--gold);
    margin-top: 22px;
  }
  .tagline {
    position: absolute; left: 144px; top: 396px; width: 460px; text-align: center;
    font-style: italic; font-weight: 700; font-size: 24px; line-height: 1.3; color: var(--cream);
    text-shadow: 0 2px 4px rgba(0,0,0,.6);
  }
  .feature-piece {
    position: absolute; left: 612px; top: 55px; width: 460px; height: 480px;
    border-radius: 48% 48% 46% 46%;
    background: radial-gradient(ellipse at 50% 60%, #e9e2d2 0%, #bfb39c 35%, #2f5a48 55%, rgba(74,42,25,0) 72%);
  }

  /* Section buttons */
  .sections { position: absolute; top: 523px; left: 0; width: 1200px; height: 106px; }
  .section-link {
    position: absolute; top: 0; height: 106px;
    font-family: "Great Vibes", cursive; color: var(--gold); text-align: center;
    display: flex; align-items: center; justify-content: center;
    background: linear-gradient(180deg, #3a2014, #1f0f08);
    box-shadow: 0 4px 10px rgba(0,0,0,.5);
  }
  .section-link span { position: relative; z-index: 1; line-height: .9; text-shadow: 0 2px 3px #000; }
  .section-link svg { position: absolute; right: -34px; top: 0; }
  .section-link.jewellery { left: 211px; width: 232px; font-size: 50px; }
  .section-link.homeware { left: 468px; width: 270px; font-size: 46px; }
  .section-link.shop { left: 792px; width: 238px; font-size: 36px; }

  /* Footer */
  .site-footer {
    position: absolute; left: 0; top: 648px; width: 1200px; height: 182px;
    background: var(--footer); box-shadow: 0 -3px 8px rgba(0,0,0,.45);
  }
  .footer-heading { font-size: 15px; color: var(--muted); margin-bottom: 8px; }
  .quick-links { position: absolute; left: 173px; top: 18px; }
  .quick-links ul { list-style: none; }
  .quick-links li { font-size: 12px; line-height: 17px; color: var(--muted); }
  .newsletter { position: absolute; left: 353px; top: 18px; width: 210px; }
  .newsletter p { font-size: 11px; line-height: 15px; color: var(--muted); margin-bottom: 8px; }
  .signup { display: flex; gap: 4px; }
  .signup .field {
    width: 136px; height: 20px; font-size: 10px; line-height: 18px; padding-left: 5px;
    background: var(--field); border: 1px solid var(--field-line); color: #7e6650;
  }
  .btn {
    height: 20px; padding: 0 7px; font-size: 11px; line-height: 18px; color: var(--cream);
    background: linear-gradient(180deg, #7a5234, #4a2c19); border: 1px solid #8a6a4a;
  }
  .social { display: flex; gap: 10px; margin-top: 14px; align-items: center; }
  .social .dot { width: 14px; height: 14px; background: var(--muted); }
  .contact { position: absolute; left: 593px; top: 18px; width: 200px; }
  .contact .field {
    display: block; width: 196px; height: 18px; margin-bottom: 6px; font-size: 10px; line-height: 16px;
    padding-left: 5px; background: var(--field); border: 1px solid var(--field-line); color: #7e6650;
  }
  .contact .field.message { height: 38px; }
  .footer-brand {
    position: absolute; left: 830px; top: 40px; width: 240px; text-align: center;
    font-family: "Cinzel", Georgia, serif; font-size: 30px; line-height: 1.15; color: var(--cream);
  }
  .copyright {
    position: absolute; left: 830px; top: 146px; width: 240px; text-align: center;
    font-size: 11px; color: var(--muted);
  }
</style>
</head>
<body>

<nav class="site-nav">
  <ul>
    <li class="is-current">Home</li>
    <li>About the artist</li>
    <li>Custom Jewellery</li>
    <li>Home Ware</li>
    <li>Shop Online</li>
    <li>Blog</li>
    <li>Contact Us</li>
  </ul>
  <div class="search">
    <div class="search-field"></div>
    <div class="search-go">Go</div>
  </div>
</nav>

<header class="brand">
  <div class="brand-name">Studio<br>Kelvara</div>
  <span class="brand-mark"></span>
</header>

<p class="tagline">Fine handcrafted Jewellery &amp; Homeware<br>Designed and produced in Jamaica<br>by Rosalind Theda Quarrington</p>

<div class="feature-piece" role="img" aria-label="Handmade statement collar necklace in cream and green stone with a leather cord"></div>

<div class="sections">
  <div class="section-link jewellery"><span>Jewellery</span>
    <svg width="40" height="106" viewBox="0 0 40 106"><path d="M2 0 L36 53 L2 106" fill="none" stroke="#e9a64a" stroke-width="5"/></svg>
  </div>
  <div class="section-link homeware"><span>Home<br>Ware</span>
    <svg width="40" height="106" viewBox="0 0 40 106"><path d="M2 0 L36 53 L2 106" fill="none" stroke="#e9a64a" stroke-width="5"/></svg>
  </div>
  <div class="section-link shop"><span>Shop Online<br>Coming soon...</span>
    <svg width="40" height="106" viewBox="0 0 40 106"><path d="M2 0 L36 53 L2 106" fill="none" stroke="#e9a64a" stroke-width="5"/></svg>
  </div>
</div>

<footer class="site-footer">
  <section class="quick-links">
    <h3 class="footer-heading">Quick Links</h3>
    <ul>
      <li>Home</li>
      <li>About the artist</li>
      <li>Custom Jewellery</li>
      <li>Home Ware</li>
      <li>Shop Online</li>
      <li>Blog</li>
      <li>Contact Us</li>
    </ul>
  </section>

  <section class="newsletter">
    <h3 class="footer-heading">Newsletter</h3>
    <p>Join our list for new pieces, studio notes and launch news from the bench.</p>
    <div class="signup">
      <div class="field">Your email address</div>
      <div class="btn">Subscribe</div>
    </div>
    <div class="social">
      <span class="dot"></span>
      <span class="dot"></span>
      <svg width="16" height="12" viewBox="0 0 16 12" aria-label="Email"><rect x="0.5" y="0.5" width="15" height="11" fill="none" stroke="#b89a78"/><path d="M0.5 0.5 L8 7 L15.5 0.5" fill="none" stroke="#b89a78"/></svg>
    </div>
  </section>

  <section class="contact">
    <h3 class="footer-heading">Contact Us</h3>
    <div class="field">Name</div>
    <div class="field">Email</div>
    <div class="field message">Message</div>
    <div class="btn" style="display:inline-block">Submit</div>
  </section>

  <div class="footer-brand">Studio<br>Kelvara</div>
  <p class="copyright">(2012) Studio Kelvara, Inc. All Rights Reserved.</p>
</footer>

</body>
</html>
```